Up and coming writing company needs a wordpress site. Our company is called PEN LOFT

We need to get a wordpress site up so that we can continue to grow our business. We already have a growing list of clients, but we want to expand beyond our existing contact list. We want our site to have a vintage feel (old typewriters, antiques, etc.). We want it to feel unique and quirky.

We love this website's look and feel: http://quillmarsh.example/

Colors
d0ebe7
e9f1ce
fee4d5

Requirements
Must have
• a button that says US
a button that says YOU
a button that says THEM
All three of those buttons need to have space underneath them for additional text. They are going to be the click options in the website
The website should say PEN LOFT at the top with the logo
Underneath it should say "We help you say what you want to say the way you want to say it."
Nice to have
• A cool antique picture (typewriter, sewing machine, etc), perhaps as a backdrop
Should not have
• Busyness.

```html
<!DOCTYPE html>
<html lang="en">
<head>
<meta charset="utf-8">
<title>PEN LOFT</title>
<link rel="stylesheet" href="https://fonts.googleapis.com/css2?family=Arimo:wght@700&family=Cabin:wght@400;500&display=swap">
<style>
  :root {
    --page-bg: #ffffff;
    --wood-dark: #1c130f;
    --wood-mid: #3b2a21;
    --teal-body: #4f8d87;
    --teal-deep: #2e5b57;
    --text-light: #ffffff;
    --text-dark: #2a1f1a;
    --mark-cream: #f1e4c8;
    --mark-ring: #4f7671;
  }
  * { margin: 0; padding: 0; box-sizing: border-box; }
  html, body {
    width: 1200px;
    height: 730px;
    overflow: hidden;
    background: var(--page-bg);
  }
  .page {
    position: relative;
    width: 1200px;
    height: 730px;
    background: var(--page-bg);
  }
  .hero {
    position: absolute;
    left: 0;
    top: 0;
    width: 1200px;
    height: 652px;
    overflow: hidden;
    background: linear-gradient(180deg, var(--wood-mid) 0%, var(--wood-dark) 100%);
  }
  .hero-photo {
    position: absolute;
    left: 324px;
    top: 54px;
    width: 570px;
    height: 510px;
    border-radius: 60px 60px 40px 40px;
    background:
      radial-gradient(ellipse 70% 60% at 50% 45%, var(--teal-body) 0%, var(--teal-deep) 70%, rgba(46,91,87,0.6) 100%);
    filter: blur(14px);
    opacity: 0.85;
  }
  .hero-shade {
    position: absolute;
    inset: 0;
    background: rgba(15, 10, 8, 0.28);
  }
  .brand {
    position: absolute;
    left: 44px;
    top: 28px;
    display: flex;
    align-items: center;
    gap: 14px;
  }
  .brand-dot {
    width: 56px;
    height: 56px;
    border-radius: 50%;
    background: var(--mark-cream);
    border: 4px solid var(--mark-ring);
  }
  .brand-name {
    font-family: "Cabin", sans-serif;
    font-weight: 500;
    font-size: 24px;
    letter-spacing: 5px;
    color: var(--text-light);
  }
  .nav-option {
    position: absolute;
    top: 224px;
    width: 340px;
    margin-left: -170px;
    text-align center;
    text-align: center;
    color: var(--text-light);
    text-decoration: none;
  }
  .nav-option--us { left: 236px; }
  .nav-option--you { left: 612px; }
  .nav-option--them { left: 1018px; }
  .nav-title {
    display: block;
    font-family: "Arimo", sans-serif;
    font-weight: 700;
    font-size: 52px;
    line-height: 58px;
    text-shadow: 0 3px 6px rgba(0,0,0,0.75);
  }
  .nav-caption {
    display: block;
    margin-top: 2px;
    font-family: "Cabin", sans-serif;
    font-weight: 400;
    font-size: 18px;
    line-height: 22px;
    text-shadow: 0 1px 3px rgba(0,0,0,0.6);
  }
  .tagline {
    position: absolute;
    left: 0;
    top: 676px;
    width: 1200px;
    text-align: center;
    font-family: "Cabin", sans-serif;
    font-weight: 400;
    font-size: 20px;
    color: var(--text-dark);
  }
</style>
</head>
<body>
  <div class="page">
    <header class="hero">
      <div class="hero-photo" role="img" aria-label="Backdrop photo: a vintage teal typewriter seen from above on a dark wooden table"></div>
      <div class="hero-shade"></div>

      <div class="brand">
        <span class="brand-dot"></span>
        <span class="brand-name">PEN LOFT</span>
      </div>

      <a class="nav-option nav-option--us" href="#us">
        <span class="nav-title">US</span>
        <span class="nav-caption">Who we are + what we do</span>
      </a>
      <a class="nav-option nav-option--you" href="#you">
        <span class="nav-title">YOU</span>
        <span class="nav-caption">Submit your project or question</span>
      </a>
      <a class="nav-option nav-option--them" href="#them">
        <span class="nav-title">THEM</span>
        <span class="nav-caption">What other people are saying about us</span>
      </a>
    </header>

    <p class="tagline">We help you say what you want to say the way you want to say it.</p>
  </div>
</body>
</html>
```